Personal Injury Book Ad Photo Set

I need a series of images for a Threadloop ad campaign for promoting a book titled "Making Sense of an Accident Claim".

```html
<!DOCTYPE html>
<html lang="en">
<head>
<meta charset="utf-8">
<title>Making Sense of an Accident Claim — Threadloop</title>
<link rel="stylesheet" href="https://fonts.googleapis.com/css2?family=Playfair+Display:wght@400;500&display=swap">
<style>
  :root {
    --ink: #231f20;
    --sky: #27a9e1;
    --mist: #d9d9db;
    --photo-dark: #3a4048;
    --photo-light: #c9ccd0;
  }
  * { margin: 0; padding: 0; box-sizing: border-box; }
  html, body { width: 1200px; height: 1200px; overflow: hidden; background: var(--ink); }
  .ad {
    position: relative;
    width: 1200px;
    height: 1200px;
    background: var(--ink);
    overflow: hidden;
  }
  .ad__photo {
    position: absolute;
    left: 0; top: 0;
    width: 1200px; height: 720px;
    background: linear-gradient(160deg, var(--photo-dark) 0%, #5b6470 38%, var(--photo-light) 62%, #8a9099 100%);
  }
  .ad__shapes {
    position: absolute;
    left: 0; top: 0;
    width: 1200px; height: 1200px;
  }
  .ad__title {
    position: absolute;
    left: 0; right: 0;
    top: 700px;
    text-align: center;
    font-family: "Playfair Display", Georgia, serif;
    font-weight: 400;
    font-size: 124px;
    line-height: 112px;
    letter-spacing: -1px;
  }
  .ad__title span { display: block; }
  .ad__title .accent { color: var(--sky); }
  .ad__title .muted { color: var(--mist); }
  .ad__title .quote { color: var(--mist); font-size: 150px; vertical-align: -6px; }
</style>
</head>
<body>
  <main class="ad">
    <div class="ad__photo" role="img" aria-label="Close-up photo of a person in a light blue shirt signing paperwork with a pen at a desk"></div>

    <svg class="ad__shapes" viewBox="0 0 833 833" aria-hidden="true">
      <polygon class="band-top" fill="var(--sky)" points="0,310 472,312 555,370 125,347 0,330"/>
      <polygon class="band-left" fill="var(--sky)" points="0,330 125,347 290,395 0,465"/>
      <polygon class="band-mid" fill="var(--mist)" points="125,347 555,370 585,482 290,395"/>
      <polygon class="band-right" fill="var(--sky)" points="555,370 833,288 833,300 585,482"/>
      <polygon class="ground" fill="var(--ink)" points="0,465 290,395 585,482 833,300 833,833 0,833"/>
    </svg>

    <h1 class="ad__title">
      <span class="accent"><span class="quote" style="display:inline">"</span>Making Sense</span>
      <span class="muted">of an Accident</span>
      <span class="accent">Claim<span class="quote" style="display:inline">"</span></span>
    </h1>
  </main>
</body>
</html>
```